Business card for home decor store and design

I need a business card for my home decor boutique that’s professional looking boho/rustic. We sell vintage furniture, vintage finds, lamps, throws, rugs. We also carry a Diy paint line for refinishing furniture. We offer workshop on painting furniture, private or group setting. We in the heart of Old Town Red Bluff. We love to design, build and restore. Family owned small business. Our style is rustic boho farmhouse. We search for one of a kind found and repurposed items. We love vintage home decor, vintage windows.

Target Market(s)

Home decor

Industry/Entity Type

Home Accessories

Contact Information for Business Card

Have a rustic look/boho

Font styles to use
Serif
Script

Requirements
Must have
• Logo

```html
<!DOCTYPE html>
<html lang="en">
<head>
<meta charset="utf-8">
<title>Hearth &amp; Willow Co. – Business Card</title>
<link href="https://fonts.googleapis.com/css2?family=Lora:wght@400;700&display=swap" rel="stylesheet">
<style>
  :root {
    --backdrop: #1c1c1c;
    --card-dark: #0d0d0d;
    --card-light: #ffffff;
    --ink: #111111;
    --silver: #d4d4d4;
    --silver-soft: #9a9a9a;
    --paper-text: #f2f2f2;
  }
  * { margin: 0; padding: 0; box-sizing: border-box; }
  html, body {
    width: 1200px; height: 1200px; overflow: hidden;
    background: var(--backdrop);
    font-family: 'Lora', Georgia, serif;
  }
  .canvas {
    width: 1200px; height: 1200px;
    display: flex; flex-direction: column; align-items: center; justify-content: center;
    gap: 50px;
  }
  .card {
    width: 860px; height: 491px; position: relative;
    box-shadow: 0 18px 40px rgba(0,0,0,.55);
  }
  .card--front { background: var(--card-dark); }
  .card--back { background: var(--card-light); color: var(--ink); }

  .brand {
    display: flex; align-items: center; gap: 18px;
    font-family: 'Lora', Georgia, serif; font-weight: 400;
    white-space: nowrap;
  }
  .brand__dot { border-radius: 50%; flex: none; }
  .card--front .brand {
    position: absolute; left: 50%; top: 200px; transform: translate(-50%, -50%);
    font-size: 46px; color: var(--silver);
  }
  .card--front .brand__dot { width: 22px; height: 22px; background: var(--silver); }
  .front__web {
    position: absolute; left: 0; right: 0; top: 392px; text-align: center;
    color: var(--paper-text); font-size: 19px; letter-spacing: 0.55em;
  }

  .card--back .brand {
    position: absolute; left: 50px; top: 245px; transform: translateY(-50%);
    font-size: 33px; color: var(--ink); gap: 12px;
  }
  .card--back .brand__dot { width: 16px; height: 16px; background: var(--ink); }
  .divider {
    position: absolute; left: 398px; top: 115px; width: 2px; height: 265px; background: var(--ink);
  }
  .contact { position: absolute; left: 458px; top: 118px; }
  .contact__name { font-weight: 700; font-size: 30px; letter-spacing: .03em; line-height: 1.05; }
  .contact__role { font-size: 20px; margin-bottom: 22px; }
  .contact__address { font-size: 22px; line-height: 1.2; margin-bottom: 18px; }
  .contact__list { list-style: none; font-size: 21px; line-height: 1.45; }
  .contact__list li { display: flex; align-items: center; gap: 14px; }
  .contact__icon { width: 20px; height: 20px; flex: none; }
</style>
</head>
<body>
<main class="canvas">
  <section class="card card--front" aria-label="Card front">
    <div class="brand"><span class="brand__dot"></span>Hearth &amp; Willow Co.</div>
    <p class="front__web">www.hearthwillow.com</p>
  </section>

  <section class="card card--back" aria-label="Card back">
    <div class="brand"><span class="brand__dot"></span>Hearth &amp; Willow Co.</div>
    <div class="divider"></div>
    <div class="contact">
      <h1 class="contact__name">NORA WHITFIELD</h1>
      <p class="contact__role">Director</p>
      <p class="contact__address">PO BOX 408, Walnut Lane<br>2nd Street, Brookvale</p>
      <ul class="contact__list">
        <li>
          <svg class="contact__icon" viewBox="0 0 24 24" aria-hidden="true"><path fill="currentColor" d="M6.6 10.8a15.1 15.1 0 0 0 6.6 6.6l2.2-2.2a1 1 0 0 1 1-.25 11.4 11.4 0 0 0 3.6.57 1 1 0 0 1 1 1V20a1 1 0 0 1-1 1A17 17 0 0 1 3 4a1 1 0 0 1 1-1h3.5a1 1 0 0 1 1 1c0 1.25.2 2.45.57 3.57a1 1 0 0 1-.25 1z"/></svg>
          +1 555 014 2270
        </li>
        <li>
          <svg class="contact__icon" viewBox="0 0 24 24" aria-hidden="true"><rect x="2" y="5" width="20" height="14" fill="currentColor"/><path d="M2 5l10 8 10-8" fill="none" stroke="#fff" stroke-width="1.6"/></svg>
          hello@hearthwillow.com
        </li>
        <li>
          <svg class="contact__icon" viewBox="0 0 24 24" aria-hidden="true"><g fill="none" stroke="currentColor" stroke-width="1.6"><circle cx="12" cy="12" r="9.5"/><ellipse cx="12" cy="12" rx="4" ry="9.5"/><path d="M2.5 12h19M4 7h16M4 17h16"/></g></svg>
          www.hearthwillow.com
        </li>
      </ul>
    </div>
  </section>
</main>
</body>
</html>
```